Brightfield Chiropractic Business Cards

Business cards with new logo design. Will upload copy of current card. We like the layout, but we need a new logo. Family, husband holding up baby toward sky, mom and other child standing next to him. We will probably want to include a catch phrase with logo. TBD

```html
<!DOCTYPE html>
<html lang="en">
<head>
<meta charset="utf-8">
<title>Brightfield Chiropractic Business Cards</title>
<link href="https://fonts.googleapis.com/css2?family=Open+Sans:wght@400;600;700&display=swap" rel="stylesheet">
<style>
  :root {
    --stage: #2a2b2e;
    --card-dark: #343538;
    --card-dark-edge: #2b2c2f;
    --brand-orange: #e8681c;
    --brand-orange-deep: #d85a12;
    --ink-light: #ffffff;
    --ink-muted: #d9d9d9;
    --map-paper: #f4f4f2;
  }
  * { box-sizing: border-box; margin: 0; padding: 0; }
  html, body {
    width: 1200px; height: 898px; overflow: hidden;
    background: var(--stage);
    font-family: "Open Sans", Arial, sans-serif;
  }
  .sheet {
    position: relative; width: 1200px; height: 898px;
    display: flex; justify-content: center; align-items: center; gap: 90px;
  }
  .card {
    position: relative; width: 340px; height: 595px;
    border-radius: 22px; overflow: hidden;
    color: var(--ink-light);
  }
  .card--front {
    background: linear-gradient(160deg, var(--card-dark), var(--card-dark-edge));
    display: flex; flex-direction: column; align-items: center; text-align: center;
  }
  .brand {
    margin-top: 150px;
    display: flex; align-items: center; gap: 12px;
  }
  .brand__dot {
    width: 22px; height: 22px; border-radius: 50%;
    background: var(--brand-orange); flex: none;
  }
  .brand__name {
    font-weight: 700; font-size: 27px; line-height: 1.08;
    letter-spacing: 0.5px; text-transform: uppercase; text-align: left;
    color: var(--ink-light);
  }
  .person { margin-top: 62px; }
  .person__name { font-size: 19px; font-weight: 600; }
  .person__role { font-size: 15px; color: var(--ink-muted); margin-top: 2px; }
  .front-contact { margin-top: 34px; font-size: 15px; line-height: 1.45; color: var(--ink-muted); }

  .card--back {
    background: linear-gradient(165deg, var(--brand-orange), var(--brand-orange-deep));
    text-align: center;
  }
  .location-map {
    position: absolute; left: 24px; top: 24px;
    width: 292px; height: 300px; border-radius: 18px;
    background: var(--map-paper);
  }
  .address {
    position: absolute; left: 0; right: 0; top: 372px;
    font-size: 15px; line-height: 1.45;
  }
  .back-contact {
    position: absolute; left: 0; right: 0; top: 450px;
    font-size: 15px; line-height: 1.45;
  }
</style>
</head>
<body>
<main class="sheet">
  <section class="card card--front" aria-label="Business card front">
    <div class="brand">
      <span class="brand__dot"></span>
      <span class="brand__name">Brightfield<br>Chiropractic</span>
    </div>
    <div class="person">
      <p class="person__name">Dr. Daniel R. Ashford</p>
      <p class="person__role">Chiropractic Physician</p>
    </div>
    <div class="front-contact">
      <p>555-014-7786</p>
      <p>AshfordChiropractic.com</p>
    </div>
  </section>

  <section class="card card--back" aria-label="Business card back">
    <div class="location-map" role="img" aria-label="Street map showing the clinic location near the town center"></div>
    <div class="address">
      <p>4820 SE Meadow Crest Center Dr.</p>
      <p>Fernhill, Oregon 97000</p>
    </div>
    <div class="back-contact">
      <p>555-014-7786</p>
      <p>Fax 555-014-7191</p>
      <p>info@drashford.com</p>
    </div>
  </section>
</main>
</body>
</html>
```